Business Cards for a small business advisory (business services)

Professional look. Same as would apply for a lawyer, accountant, or other financial services professional. Please use the logo colors

Target Market(s)

small business owners

Industry/Entity Type

Financial Servics

Contact Information for Business Card

Name: Gavin L. Whitmore, CAIA / Title: Business Advisor / Office #: (718) 294-7716 / Mobile #: (917) 382-5047 / Email: g.whitmore@clearfieldventurepartners.example / Web: www.clearfieldventurepartners.example

Font styles to use
Sans Serif

```html
<!DOCTYPE html>
<html lang="en">
<head>
<meta charset="utf-8">
<title>Clearfield Venture Partners – Business Cards</title>
<link href="https://fonts.googleapis.com/css2?family=Montserrat:wght@400;500;600;700&display=swap" rel="stylesheet">
<style>
  :root {
    --page-bg: #d4d5d7;
    --navy: #1b3a6b;
    --navy-deep: #173262;
    --green: #7dc242;
    --white: #ffffff;
    --mist: #dfe4ec;
    --text-dark: #1d3461;
  }
  * { margin: 0; padding: 0; box-sizing: border-box; }
  html, body {
    width: 900px; height: 1200px; overflow: hidden;
    background: var(--page-bg);
    font-family: "Montserrat", sans-serif;
  }
  .card {
    position: absolute; left: 135px; width: 631px; height: 358px; overflow: hidden;
  }
  .card-front {
    top: 215px;
    background: linear-gradient(135deg, var(--navy-deep), var(--navy));
  }
  .card-back { top: 628px; background: var(--white); }

  .brand-mark {
    position: absolute; border-radius: 50%; background: var(--green);
  }
  .card-front .brand-mark { left: 104px; top: 139px; width: 80px; height: 80px; }
  .card-front .brand-name {
    position: absolute; left: 198px; top: 136px;
    color: var(--white); font-weight: 600; font-size: 36px; line-height: 38px;
    letter-spacing: 0.2px;
  }
  .card-front .brand-tagline {
    position: absolute; left: 199px; top: 222px;
    color: var(--white); font-weight: 600; font-size: 7.6px; letter-spacing: 0.2px;
    text-transform: uppercase; white-space: nowrap;
  }

  .card-back .brand-mark { left: 40px; top: 45px; width: 46px; height: 46px; }
  .card-back .brand-name {
    position: absolute; left: 98px; top: 40px;
    color: var(--navy); font-weight: 600; font-size: 21px; line-height: 22px;
  }
  .card-back .brand-tagline {
    position: absolute; left: 99px; top: 88px;
    color: var(--navy); font-weight: 600; font-size: 4.6px;
    text-transform: uppercase; white-space: nowrap;
  }
  .decor-disc {
    position: absolute; left: 396px; top: 36px; width: 250px; height: 250px;
    border-radius: 50%; background: var(--mist); opacity: 0.6;
  }
  .person-name {
    position: absolute; left: 99px; top: 164px;
    color: var(--text-dark); font-weight: 600; font-size: 25px;
  }
  .person-title {
    position: absolute; left: 100px; top: 198px;
    color: var(--green); font-weight: 400; font-size: 15px;
  }
  .contact-list {
    position: absolute; left: 104px; top: 242px; list-style: none;
  }
  .contact-list li {
    display: flex; align-items: center; height: 22.5px;
    color: var(--text-dark); font-size: 15px; letter-spacing: 0.9px;
  }
  .contact-list li.email, .contact-list li.web { font-size: 14px; letter-spacing: 0.4px; }
  .contact-list svg { width: 13px; height: 13px; margin-right: 8px; flex: none; fill: var(--green); }
</style>
</head>
<body>
  <section class="card card-front">
    <span class="brand-mark"></span>
    <div class="brand-name">Clearfield<br>Venture Partners</div>
    <div class="brand-tagline">Steady counsel for owners planning the next chapter of their firm</div>
  </section>

  <section class="card card-back">
    <span class="decor-disc"></span>
    <span class="brand-mark"></span>
    <div class="brand-name">Clearfield<br>Venture Partners</div>
    <div class="brand-tagline">Steady counsel for owners planning the next chapter of their firm</div>

    <h1 class="person-name">Gavin L. Whitmore, CAIA</h1>
    <p class="person-title">Business Advisor</p>

    <ul class="contact-list">
      <li class="office">
        <svg viewBox="0 0 24 24"><path d="M6.6 10.8a15 15 0 0 0 6.6 6.6l2.2-2.2c.3-.3.7-.4 1-.2 1.1.4 2.3.6 3.6.6.6 0 1 .4 1 1V20c0 .6-.4 1-1 1A17 17 0 0 1 3 4c0-.6.4-1 1-1h3.5c.6 0 1 .4 1 1 0 1.3.2 2.5.6 3.6.1.3 0 .7-.2 1z"/></svg>
        (718) 294-7716
      </li>
      <li class="mobile">
        <svg viewBox="0 0 24 24"><path d="M7 1h10a2 2 0 0 1 2 2v18a2 2 0 0 1-2 2H7a2 2 0 0 1-2-2V3a2 2 0 0 1 2-2zm0 3v15h10V4z"/></svg>
        (917) 382-5047
      </li>
      <li class="email">
        <svg viewBox="0 0 24 24"><path d="M2 5h20v14H2zm2 2v.5l8 5 8-5V7z"/></svg>
        g.whitmore@clearfieldventurepartners.example
      </li>
      <li class="web">
        <svg viewBox="0 0 24 24"><path d="M12 2a10 10 0 1 0 0 20 10 10 0 0 0 0-20zm-1 2.1V8H7.4A8 8 0 0 1 11 4.1zm2 0A8 8 0 0 1 16.6 8H13zM4.3 10H11v4H4.3a8 8 0 0 1 0-4zm8.7 0h6.7a8 8 0 0 1 0 4H13zm-5.6 6H11v3.9A8 8 0 0 1 7.4 16zm5.6 0h3.6a8 8 0 0 1-3.6 3.9z"/></svg>
        www.clearfieldventurepartners.example
      </li>
    </ul>
  </section>
</body>
</html>
```